Business Card Design for Occupational Medicine Start Up Company

We need to design a professional business card. We are a healthcare company providing occupational medicine services to blue collar industries. We are professional, efficient and high quality service providers.

Target Market(s)

Blue Collar Industry: Shipbuilding, Ports, Trucking Companies; The Executives and Safety Officers for these companies

Industry/Entity Type

Healthcare

Contact Information for Business Card

Logo, Name, Title, Email, Phone

Other font styles liked:
• Please match our Brand Guide

Requirements
Must have
• Our Company Colors and Logo

```html
<!DOCTYPE html>
<html lang="en">
<head>
<meta charset="utf-8">
<title>Shiftwell Clinics – Business Card</title>
<link href="https://fonts.googleapis.com/css2?family=Montserrat:wght@400;600;700&family=Arimo:wght@400&display=swap" rel="stylesheet">
<style>
  :root {
    --navy: #2a3580;
    --sky: #22a7df;
    --amber: #f4b041;
    --paper: #ffffff;
    --ink: #1c1c1c;
    --backdrop: #5d5d5d;
  }
  * { margin: 0; padding: 0; box-sizing: border-box; }
  html, body { width: 1075px; height: 1200px; overflow: hidden; }
  body { background: var(--backdrop); position: relative; font-family: "Arimo", Arial, sans-serif; }

  .card { position: absolute; left: 206px; width: 663px; height: 395px; overflow: hidden; }
  .card-front { top: 187px; background: var(--paper); }
  .card-back { top: 637px; background: var(--navy); }

  /* brand name set as text */
  .brand { position: absolute; text-align: center; font-family: "Montserrat", Arial, sans-serif; font-weight: 700; }
  .brand-dot { display: block; margin: 0 auto; border-radius: 50%; }
  .brand-name { display: block; letter-spacing: 0.5px; line-height: 1; }
  .brand-sub { display: block; letter-spacing: 7px; line-height: 1; }

  .card-front .brand { left: 320px; top: 56px; width: 340px; color: var(--navy); }
  .card-front .brand-dot { width: 80px; height: 80px; background: var(--navy); }
  .card-front .brand-name { font-size: 35px; margin-top: 26px; }
  .card-front .brand-sub { font-size: 20px; margin-top: 6px; }

  .holder { position: absolute; left: 35px; top: 218px; }
  .holder-name { font-family: "Montserrat", Arial, sans-serif; font-weight: 700; font-size: 26px; color: var(--navy); line-height: 1; }
  .holder-title { font-size: 16px; color: var(--ink); margin-top: 6px; letter-spacing: 0.2px; }
  .holder-rule { position: absolute; left: 35px; top: 276px; width: 237px; height: 4px; background: var(--sky); }

  .contact-band { position: absolute; left: 0; top: 279px; width: 100%; height: 116px; background: var(--navy); color: var(--paper); }
  .contact-list { position: absolute; left: 35px; top: 22px; list-style: none; font-size: 18px; }
  .contact-list li { display: flex; align-items: center; height: 24px; }
  .contact-list svg { width: 17px; height: 17px; margin-right: 6px; flex: none; }
  .address { position: absolute; right: 40px; top: 47px; text-align: right; font-size: 18px; line-height: 24px; }

  .card-back .brand { left: 0; top: 78px; width: 100%; color: var(--paper); }
  .card-back .brand-dot { width: 110px; height: 110px; background: var(--paper); }
  .card-back .brand-name { font-size: 43px; margin-top: 28px; }
  .card-back .brand-sub { font-size: 24px; margin-top: 8px; letter-spacing: 9px; }
  .web-band { position: absolute; left: 0; bottom: 0; width: 100%; height: 44px; background: var(--sky); color: var(--paper); font-size: 18px; text-align: center; line-height: 44px; }
</style>
</head>
<body>
  <section class="card card-front">
    <div class="brand">
      <span class="brand-dot"></span>
      <span class="brand-name">SHIFTWELL</span>
      <span class="brand-sub">CLINICS</span>
    </div>

    <div class="holder">
      <p class="holder-name">MARCUS REILLY</p>
      <p class="holder-title">MANAGING DIRECTOR</p>
    </div>
    <div class="holder-rule"></div>

    <div class="contact-band">
      <ul class="contact-list">
        <li>
          <svg viewBox="0 0 24 24" fill="none" stroke="var(--amber)" stroke-width="2.4" stroke-linecap="round" stroke-linejoin="round"><path d="M22 16.9v3a2 2 0 0 1-2.2 2 19.8 19.8 0 0 1-8.6-3.1 19.5 19.5 0 0 1-6-6A19.8 19.8 0 0 1 2.1 4.2 2 2 0 0 1 4.1 2h3a2 2 0 0 1 2 1.7c.1.9.4 1.8.7 2.7a2 2 0 0 1-.5 2.1L8 9.8a16 16 0 0 0 6 6l1.3-1.3a2 2 0 0 1 2.1-.4c.9.3 1.8.6 2.7.7a2 2 0 0 1 1.7 2z"/></svg>
          044-123 456 789
        </li>
        <li>
          <svg viewBox="0 0 24 24"><rect x="1" y="5" width="22" height="15" fill="var(--amber)"/><path d="M1 5l11 9 11-9" fill="none" stroke="var(--navy)" stroke-width="1.6"/></svg>
          info@webname.com
        </li>
        <li>
          <svg viewBox="0 0 24 24" fill="none" stroke="var(--amber)" stroke-width="2"><circle cx="12" cy="12" r="10"/><path d="M2 12h20M12 2c3 3 3 17 0 20M12 2c-3 3-3 17 0 20M4 7h16M4 17h16"/></svg>
          www.websitename.com
        </li>
      </ul>
      <p class="address">421, Address line goes here<br>45452,Country Name</p>
    </div>
  </section>

  <section class="card card-back">
    <div class="brand">
      <span class="brand-dot"></span>
      <span class="brand-name">SHIFTWELL</span>
      <span class="brand-sub">CLINICS</span>
    </div>
    <div class="web-band">www.websitename.com</div>
  </section>
</body>
</html>
```